Website design for Cambridge based systematic hedge fund

We have run previous craftmosaic competitions to design our company logo, business cards and the styling of our presentation deck (see attached files).
As the final step we are looking to get a website designed that is thematically consistent with these existing elements of our branding.
You can find some of our competitors websites below:
https://www.quelmarsh.example/
https://www.fenloor.example/
https://www.pyvart.example/
https://www.dulvet.example/
https://www.orbelmfunds.example/
https://www.valtrigo.example/
https://www.meskilfunds.example/home
We would like to have a website that works well on both mobile devices and desktops. Either just as one page that can be scrolled down, with links at the top that skips to certain sections, or a few separate pages that can be navigated by a top menu.
It should look professional, we are not after lots of animations or unnecessary transitions, and in particular the website must be smooth to navigate. We would like to avoid having peoples of people, we are happy to make use of elements from the presentation (for example the style of the cover slide, or the section slides with the faded bridge in the background), or 'financial' style images.
We would like to have the following sections for now. For some of these some example text has been provided, final text may change but it will be of similar length. For the other sections we are happy to just have template text for now. At the moment we are mainly interested to see styles/layouts as words can be added easily afterwards:
1) We will need a disclaimer pop up the first time someone visits the site (see for example the meskilfunds example).
2) Top page - company name, then in larger text "Bringing AI and Statistical Inference to Financial Markets", and somewhere in smaller text "Harlow Vectors is a quantitative asset manager with the singular focus of delivering algorithmic strategies that work"
3) "About us" section: will describe us as a company, details our approach, company values, and explains the company logo.
Example text:
"We deliver consistent alpha across liquid markets through the application of proprietary IP in Bayesian inference, machine learning and artificial intelligence. We are a multi-disciplinary team founded by experienced finance professionals from premier institutions, leading academics from the Thornbury Stellar Unit at Ashmere College and world-class software engineers.
Our logo portrays a sillhoute of the lattice walkway at Ashmere College. Our unique scientific approach allows us to bridge cutting-edge mathematical research and computing expertise with financial knowledge to bring algorithmns that work to liquid markets"
4) Hiring section, detailing our culture, what we are looking for.
Example text:
"We are always looking for exceptional talent to join our entrepreneurial team. We are looking for individuals who are creative thinkers, can demonstrate analytical rigour and are passionate about the intersection of science, finance and technology.
We prioritise having a company culture that promotes sharing ideas in a safe, collaborative research environment. We make sure that every member of the team has the oppertunity to explore their own ideas through weekly 'innovation time', and ensure that everyone gets the support they need to continue to grow as individuals within the company."
5) A section for news/press releases
6) Contact us area at the bottom with office location and email. We will need to list 3 addresses for our Cambridge, London and Singapore offices, along with a couple of contact emails or phone numbers
7) A client login button at the top that will take them to a different website (unrelated to this one).

```html
<!DOCTYPE html>
<html lang="en">
<head>
<meta charset="utf-8">
<title>Harlow Vectors</title>
<link rel="stylesheet" href="https://fonts.googleapis.com/css2?family=Barlow+Condensed:wght@600;700&family=Poppins:wght@300;400;500&display=swap">
<style>
:root{
  --navy:#0b3568;
  --navy-deep:#082a55;
  --accent:#5b8fd0;
  --ink:#111;
  --muted:#555;
  --faint:#eef1f5;
  --white:#fff;
}
*{box-sizing:border-box;margin:0;padding:0}
html,body{width:1200px;height:3619px;overflow:hidden}
body{position:relative;background:var(--white);font-family:'Poppins',sans-serif;color:var(--ink)}
.abs{position:absolute}
.display{font-family:'Barlow Condensed',sans-serif;font-weight:700;text-transform:uppercase;letter-spacing:.5px}
.accent{color:var(--accent)}
.photo{position:absolute}

/* hero */
.hero{position:absolute;left:0;top:0;width:1200px;height:675px;background:linear-gradient(180deg,#1f2347 0%,#3b2f55 35%,#7a4a4c 52%,#2a2640 62%,#15172c 100%)}
.brand{position:absolute;font-family:'Poppins',sans-serif;font-weight:500;color:var(--accent);font-size:20px;letter-spacing:1px;text-transform:uppercase;display:flex;align-items:center;gap:10px}
.brand i{display:block;width:14px;height:14px;background:var(--accent)}
.nav{position:absolute;left:594px;top:22px;display:flex;gap:33px;font-size:11px;color:var(--white);text-transform:uppercase}
.nav .current{color:var(--accent)}
.login{position:absolute;left:1035px;top:12px;width:105px;height:36px;background:var(--white);color:var(--ink);font-size:13px;font-weight:500;display:flex;align-items:center;justify-content:center}
.hero-title{position:absolute;left:61px;top:203px;width:580px;font-family:'Barlow Condensed',sans-serif;font-weight:700;font-size:56px;line-height:60px;color:var(--white);letter-spacing:.3px}
.hero-title .accent{text-transform:uppercase}
.hero-lead{position:absolute;left:61px;top:396px;width:410px;font-size:13.5px;line-height:23px;color:var(--white);font-weight:300}
.btn-light{position:absolute;left:60px;top:488px;width:105px;height:37px;background:var(--white);font-size:12px;font-weight:500;display:flex;align-items:center;justify-content:center;text-transform:uppercase}
.dots{position:absolute;left:60px;top:647px;display:flex;gap:6px;align-items:center}
.dots span{width:3px;height:3px;border-radius:50%;background:var(--white)}
.dots .on{width:12px;height:12px;border:1.5px solid var(--white);background:transparent}
.thumb{position:absolute;top:614px;width:72px;height:75px;border:1px solid var(--white)}

/* guides */
.guide{position:absolute;top:690px;width:1px;height:1640px;background:var(--faint)}
.vertical{position:absolute;font-family:'Barlow Condensed',sans-serif;font-weight:600;font-size:78px;color:transparent;-webkit-text-stroke:1px #e4e8ee;writing-mode:vertical-rl;transform:rotate(180deg);text-transform:uppercase;line-height:1}

.section-title{font-family:'Barlow Condensed',sans-serif;font-weight:700;font-size:32px;text-transform:uppercase}
.copy{font-size:12.5px;line-height:19.5px;color:var(--muted)}
.copy p+p{margin-top:4px}

/* hiring */
.hiring-panel{position:absolute;left:0;top:1159px;width:832px;height:419px;background:var(--navy)}
.hiring .copy{color:var(--white)}
.hiring .copy p+p{margin-top:15px}

/* contact */
.office-name{font-size:20px;font-weight:400}
.office-line{position:absolute;display:flex;gap:14px;font-size:12px;line-height:19px;color:var(--muted);width:230px}
.office-line svg{flex:none;width:16px;height:16px;margin-top:2px}

/* news */
.news{position:absolute;left:0;top:2681px;width:1200px;height:472px;background:linear-gradient(180deg,#103d74,#0c3366)}
.news-title{position:absolute;top:2736px;left:0;width:1200px;text-align:center;font-size:33px;color:var(--white)}
.card-img{position:absolute;top:2790px;width:285px;height:194px}
.tag{position:absolute;top:2894px;width:32px;height:90px;background:var(--accent);color:var(--white);font-size:10px;font-weight:500;writing-mode:vertical-rl;transform:rotate(180deg);display:flex;align-items:center;justify-content:center;text-transform:uppercase}
.card-date{position:absolute;top:3000px;font-size:12px;font-weight:500;color:var(--white)}
.card-text{position:absolute;top:3030px;width:268px;font-size:12.5px;line-height:19.5px;color:#c9d6ea;font-weight:300}

/* footer */
.foot-title{position:absolute;top:3217px;font-size:19px;color:var(--navy);font-weight:400}
.sitemap{position:absolute;left:337px;top:3258px;list-style:none;font-size:12px;color:var(--muted)}
.sitemap li{height:34.8px}
.foot-office{position:absolute;font-size:14px;color:var(--ink)}
.social{position:absolute;left:60px;top:3319px;display:flex;gap:6px}
.social span{width:33px;height:33px;border:1.5px solid var(--navy);border-radius:50%}
.legal{position:absolute;left:0;top:3580px;width:1200px;height:39px;background:var(--navy-deep);color:var(--white);font-size:11px;display:flex;align-items:center;justify-content:center}
</style>
</head>
<body>
<svg width="0" height="0" style="position:absolute">
  <symbol id="i-pin" viewBox="0 0 16 16"><path d="M8 1.5a4.5 4.5 0 0 0-4.5 4.5c0 3.4 4.5 8.5 4.5 8.5s4.5-5.1 4.5-8.5A4.5 4.5 0 0 0 8 1.5z" fill="none" stroke="#5b8fd0" stroke-width="1.5"/><circle cx="8" cy="6" r="1.6" fill="#5b8fd0"/></symbol>
  <symbol id="i-phone" viewBox="0 0 16 16"><path d="M3 1.5l2.6.3 1 3.1-1.6 1.3a8 8 0 0 0 4.8 4.8l1.3-1.6 3.1 1 .3 2.6c-.4.9-1.4 1.5-2.4 1.4C6.8 13.9 2.1 9.2 1.6 3.9 1.5 2.9 2.1 1.9 3 1.5z" fill="#5b8fd0"/></symbol>
  <symbol id="i-mail" viewBox="0 0 16 16"><rect x="1" y="3" width="14" height="10" rx="1.5" fill="#5b8fd0"/><path d="M1.8 4l6.2 4.8L14.2 4" fill="none" stroke="#fff" stroke-width="1.2"/></symbol>
</svg>

<!-- hero -->
<section class="hero" role="img" aria-label="Night view of a lit arched bridge reflected in water at dusk"></section>
<div class="brand" style="left:60px;top:38px">Harlow Vectors</div>
<nav class="nav">
  <span class="current">Home</span><span>About Us</span><span>Hiring</span><span>News/Press</span><span>Contact Us</span>
</nav>
<a class="login">LOGIN</a>
<h1 class="hero-title">Bringing AI and Statistical Inference <span class="accent">To Financial Markets</span></h1>
<p class="hero-lead">Harlow Vectors is a quantitative asset manager with the singular focus of delivering algorithmic strategies that work</p>
<a class="btn-light">Contcat Us</a>
<div class="dots"><span></span><span></span><span></span><span class="on"></span></div>
<div class="thumb" style="left:902px;background:linear-gradient(135deg,#d9d6cf,#8e8a84)" role="img" aria-label="Laptop showing financial charts"></div>
<div class="thumb" style="left:985px;background:linear-gradient(180deg,#b9c6d2,#b8503c 55%,#6e7a86)" role="img" aria-label="Red suspension bridge"></div>
<div class="thumb" style="left:1068px;background:linear-gradient(180deg,#7fa1ae,#3e4a46)" role="img" aria-label="Stone arch bridge over a coastal road"></div>
<div class="abs" style="left:135px;top:674px;width:337px;height:4px;background:var(--accent)"></div>

<div class="guide" style="left:187px"></div>
<div class="guide" style="left:555px"></div>
<div class="guide" style="left:922px"></div>

<!-- about -->
<section class="about">
  <div class="vertical" style="left:60px;top:752px;height:331px">About Us</div>
  <h2 class="section-title abs" style="left:159px;top:773px">About <span class="accent">Us</span></h2>
  <div class="copy abs" style="left:152px;top:815px;width:400px">
    <p>"We deliver consistent alpha across liquid markets through the application of proprietary IP in Bayesian inference, machine learning and artificial intelligence. We are a multi-disciplinary team founded by experienced finance professionals from premier institutions, leading academics from the Thornbury Stellar Unit at Ashmere College and world-class software engineers.</p>
    <p>Our logo portrays a sillhoute of the lattice walkway at Ashmere College. Our unique scientific approach allows us to bridge cutting-edge mathematical research and computing expertise with financial knowledge to bring algorithmns that work to liquid markets</p>
  </div>
  <div class="abs" style="left:1050px;top:864px;width:5px;height:220px;background:var(--accent)"></div>
  <div class="photo" style="left:689px;top:755px;width:361px;height:329px;background:linear-gradient(180deg,#3b2616,#a8682a 45%,#2c1c10)" role="img" aria-label="Canal street at night with warm lamplight and a small bridge"></div>
</section>

<!-- hiring -->
<section class="hiring">
  <div class="hiring-panel"></div>
  <h2 class="section-title abs" style="left:62px;top:1227px;color:var(--white)">Hiring</h2>
  <div class="copy abs" style="left:62px;top:1272px;width:375px">
    <p>We are always looking for exceptional talent to join our entrepreneurial team. We are looking for individuals who are creative thinkers, can demonstrate analytical rigour and are passionate about the intersection of science, finance and technology.</p>
    <p>We prioritise having a company culture that promotes sharing ideas in a safe, collaborative research environment. We make sure that every member of the team has the oppertunity to explore their own ideas through weekly 'innovation time', and ensure that everyone gets the support they need to continue to grow as individuals within the company.</p>
  </div>
  <div class="abs" style="left:733px;top:1553px;width:187px;height:4px;background:var(--accent)"></div>
  <div class="photo" style="left:509px;top:1180px;width:411px;height:373px;background:linear-gradient(135deg,#2b2522,#5a514b 50%,#1b1715)" role="img" aria-label="Team member working on a tablet at a desk"></div>
  <div class="vertical" style="left:966px;top:1290px;height:228px">Hiring</div>
</section>

<!-- contact -->
<section class="contact">
  <h2 class="section-title abs" style="left:0;top:1642px;width:1200px;text-align:center">Contact <span class="accent">Us</span></h2>
  <div class="vertical" style="left:76px;top:1904px;height:407px">Contact Us</div>

  <div class="abs" style="left:222px;top:1725px;width:345px;height:320px;border-left:4px solid var(--accent);border-bottom:4px solid var(--accent)"></div>
  <div class="photo" style="left:226px;top:1725px;width:337px;height:315px;background:linear-gradient(180deg,#a9c0d8,#8f8374 45%,#4b4a3e)" role="img" aria-label="Wooden lattice footbridge over a river beside college buildings"></div>

  <div class="abs office-name" style="left:652px;top:1782px">Cambridge</div>
  <div class="office-line" style="left:648px;top:1833px"><svg><use href="#i-pin"/></svg>101- Lorem Ipsum is simply dummy text of the</div>
  <div class="office-line" style="left:648px;top:1881px"><svg><use href="#i-phone"/></svg>(+44) 100 200 3000</div>
  <div class="office-line" style="left:648px;top:1915px"><svg><use href="#i-mail"/></svg>info@harlowvectors.example</div>

  <div class="abs" style="left:636px;top:2011px;width:342px;height:316px;border-right:4px solid var(--accent);border-bottom:4px solid var(--accent)"></div>
  <div class="photo" style="left:636px;top:2011px;width:338px;height:314px;background:linear-gradient(180deg,#b9c7d2,#7e7f7c 50%,#3e4b55)" role="img" aria-label="Gothic towered bridge over a river with city skyline"></div>

  <div class="abs office-name" style="left:355px;top:2082px">London</div>
  <div class="office-line" style="left:351px;top:2134px"><svg><use href="#i-pin"/></svg>101- Lorem Ipsum is simply dummy text of the</div>
  <div class="office-line" style="left:351px;top:2181px"><svg><use href="#i-phone"/></svg>(+44) 100 200 3000</div>
  <div class="office-line" style="left:351px;top:2215px"><svg><use href="#i-mail"/></svg>info@harlowvectors.example</div>

  <div class="abs" style="left:215px;top:2289px;width:341px;height:317px;border-left:4px solid var(--accent);border-bottom:4px solid var(--accent)"></div>
  <div class="photo" style="left:219px;top:2289px;width:337px;height:313px;background:linear-gradient(180deg,#c8a7b8,#8f7f86 45%,#3f3a40)" role="img" aria-label="Dense high-rise city skyline at dusk"></div>

  <div class="abs office-name" style="left:652px;top:2390px">Singapore</div>
  <div class="office-line" style="left:648px;top:2440px"><svg><use href="#i-pin"/></svg>101- Lorem Ipsum is simply dummy text of the</div>
  <div class="office-line" style="left:648px;top:2488px"><svg><use href="#i-phone"/></svg>(+44) 100 200 3000</div>
  <div class="office-line" style="left:648px;top:2522px"><svg><use href="#i-mail"/></svg>info@harlowvectors.example</div>
</section>

<!-- news -->
<section>
  <div class="news" role="img" aria-label="Faded bridge silhouette over deep blue background"></div>
  <h2 class="display news-title">News <span class="accent">/ Press</span></h2>

  <div class="card-img" style="left:142px;background:linear-gradient(180deg,#cfd2d3,#8a8d8c 55%,#6d5a3c)" role="img" aria-label="Stone hands holding a footbridge in mist"></div>
  <div class="tag" style="left:142px">Inteligence</div>
  <div class="card-date" style="left:143px">AUG 28, 2021 - 24 COMMENTS</div>
  <p class="card-text" style="left:143px">Lorem Ipsum is simply dummy text of the printing and typesetting industry. Lorem Ipsum has been the industry's</p>

  <div class="card-img" style="left:457px;background:linear-gradient(135deg,#f1f2f4,#c6ccd3 55%,#6f7781)" role="img" aria-label="Hands reviewing financial reports beside a laptop"></div>
  <div class="tag" style="left:457px">Bridge</div>
  <div class="card-date" style="left:458px">AUG 28, 2021 - 24 COMMENTS</div>
  <p class="card-text" style="left:458px">Lorem Ipsum is simply dummy text of the printing and typesetting industry. Lorem Ipsum has been the industry's</p>

  <div class="card-img" style="left:772px;background:linear-gradient(180deg,#d6dbde,#9a8a6e 50%,#4d5a3a)" role="img" aria-label="Gothic college chapel with graduates on the lawn"></div>
  <div class="tag" style="left:772px">Financial</div>
  <div class="card-date" style="left:773px">AUG 28, 2021 - 24 COMMENTS</div>
  <p class="card-text" style="left:773px">Lorem Ipsum is simply dummy text of the printing and typesetting industry. Lorem Ipsum has been the industry's</p>
</section>

<!-- footer -->
<footer>
  <div class="brand" style="left:60px;top:3240px;color:var(--navy)"><i style="background:var(--navy)"></i>Harlow Vectors</div>
  <div class="social" aria-label="Social links"><span></span><span></span><span></span><span></span></div>

  <div class="foot-title" style="left:337px">Site Map</div>
  <ul class="sitemap"><li>- Home</li><li>- About Us</li><li>- Hiring</li><li>- News/ Press</li><li>- Contact Us</li><li>- Login</li></ul>

  <div class="foot-title" style="left:613px">Contact Us</div>

  <div class="foot-office" style="left:613px;top:3258px">Cambridge</div>
  <div class="office-line" style="left:611px;top:3288px"><svg><use href="#i-pin"/></svg>101- Lorem Ipsum is simply dummy text of the</div>
  <div class="office-line" style="left:611px;top:3333px"><svg><use href="#i-phone"/></svg>(+44) 100 200 3000</div>
  <div class="office-line" style="left:611px;top:3363px"><svg><use href="#i-mail"/></svg>info@harlowvectors.example</div>

  <div class="foot-office" style="left:888px;top:3258px">Singapore</div>
  <div class="office-line" style="left:886px;top:3288px"><svg><use href="#i-pin"/></svg>101- Lorem Ipsum is simply dummy text of the</div>
  <div class="office-line" style="left:886px;top:3333px"><svg><use href="#i-phone"/></svg>(+44) 100 200 3000</div>
  <div class="office-line" style="left:886px;top:3363px"><svg><use href="#i-mail"/></svg>info@harlowvectors.example</div>

  <div class="foot-office" style="left:613px;top:3400px">London</div>
  <div class="office-line" style="left:611px;top:3430px"><svg><use href="#i-pin"/></svg>101- Lorem Ipsum is simply dummy text of the</div>
  <div class="office-line" style="left:611px;top:3475px"><svg><use href="#i-phone"/></svg>(+44) 100 200 3000</div>
  <div class="office-line" style="left:611px;top:3505px"><svg><use href="#i-mail"/></svg>info@harlowvectors.example</div>

  <div class="legal">© 2021 Harlowvectors.All rights reserved</div>
</footer>
</body>
</html>
```